New Restaurant Flyer more work need later!!

I am opening A new Restaurant The Copper Lantern
The theme of the restaurant is shabby chic
I have purchased 1950 furniture and the decor will be painted ( Mabel Farrow style Google Mabel Farrow.) The colours will be Tessa Greens.
I have no photos yet as the project has not started yet.
It is a pub style restaurant and the main feature is the Bar which has been built with an old altar which has been taken from a church.
The food will be all day
Breakfasts
Lunches
which will vary from sandwiches to light bites
Our Unique selling point are:
We Intend to do a grazing menu ( small plates )
The customer will maybe choose 3 as meal They will be served on wooden drift wood boards
for example
Sticky ribs Fish cakes And duck spring rolls.
Our main USP will be Steaks Fish And Chicken which will be cooked on a Wendel oven ( Google it)
Its a oven which uses real charcoal and cooked the same as you would in the summer in you garden./
We will also be selling cakes and coffee's
We will be selling traditional cask ales and fine wines.
this link is the details of the premises

http://www.brackwellagents.example/property/512?showstc=on&town=&multi_types=Restaurant+%2F+Cafe&unit_minarea=&unit_maxarea=&unit_areatype=&page=1
any questions email me
rowlinsk@mailbox.example
I will also be looking for additional marketing art work latter

Restaurant

```html
<!DOCTYPE html>
<html lang="en">
<head>
<meta charset="utf-8">
<title>The Copper Lantern – Flyer</title>
<link rel="stylesheet" href="https://fonts.googleapis.com/css2?family=Short+Stack&display=swap">
<style>
  :root {
    --ink: #ffffff;
    --night: #000000;
    --frame: #f4f4f4;
    --flame-deep: #7a1c00;
    --flame-mid: #e0530c;
    --flame-bright: #ffb21e;
    --photo-stone: #c9c3b8;
    --photo-shade: #4a3a33;
  }
  * { margin: 0; padding: 0; box-sizing: border-box; }
  html, body { width: 928px; height: 1200px; overflow: hidden; background: var(--night); }
  .flyer {
    position: relative;
    width: 928px;
    height: 1200px;
    background: var(--night);
    color: var(--ink);
    font-family: "Short Stack", "Comic Sans MS", cursive;
    overflow: hidden;
  }
  .flyer__frame { position: absolute; inset: 0; width: 928px; height: 1200px; }
  .flyer__flames {
    position: absolute;
    left: 0; right: 0; bottom: 0;
    height: 320px;
    background:
      radial-gradient(ellipse 30% 70% at 20% 100%, var(--flame-bright), transparent 70%),
      radial-gradient(ellipse 35% 80% at 60% 100%, var(--flame-bright), transparent 70%),
      radial-gradient(ellipse 25% 60% at 90% 100%, var(--flame-mid), transparent 75%),
      linear-gradient(to top, var(--flame-mid) 0%, var(--flame-deep) 45%, var(--night) 100%);
  }
  .brand {
    position: absolute;
    top: 98px; left: 0; right: 0;
    text-align: center;
    font-size: 66px;
    line-height: 1;
    color: var(--ink);
  }
  .headline {
    position: absolute;
    left: 0; right: 0;
    text-align: center;
    line-height: 1;
  }
  .headline--dishes { top: 258px; font-size: 62px; }
  .headline--method { top: 334px; font-size: 42px; }
  .headline--hours { top: 430px; font-size: 45px; }
  .premises-photo {
    position: absolute;
    left: 212px; top: 510px;
    width: 484px; height: 383px;
    background: linear-gradient(160deg, var(--photo-stone) 0%, #e8e4dc 40%, var(--photo-shade) 100%);
    box-shadow: 0 0 0 3px #ddd;
  }
  .offer {
    position: absolute;
    font-size: 33px;
    line-height: 1.05;
    text-align: center;
    transform: translate(-50%, -50%);
    white-space: nowrap;
  }
  .offer--breakfast { left: 118px; top: 572px; transform: translate(-50%, -50%) rotate(-10deg); }
  .offer--lunch { left: 124px; top: 676px; transform: translate(-50%, -50%) rotate(8deg); }
  .offer--ales { left: 116px; top: 801px; transform: translate(-50%, -50%) rotate(6deg); }
  .offer--cakes { left: 792px; top: 575px; transform: translate(-50%, -50%) rotate(8deg); }
  .offer--buffet { left: 790px; top: 691px; transform: translate(-50%, -50%) rotate(-8deg); }
  .offer--wines { left: 797px; top: 804px; transform: translate(-50%, -50%) rotate(4deg); }
  .contact {
    position: absolute;
    left: 0; right: 0; top: 935px;
    text-align: center;
    font-size: 46px;
    line-height: 1.28;
  }
</style>
</head>
<body>
<main class="flyer">
  <div class="flyer__flames" role="img" aria-label="Flames from an open charcoal grill rising along the bottom of the flyer"></div>

  <svg class="flyer__frame" viewBox="0 0 928 1200" aria-hidden="true">
    <rect x="16" y="16" width="896" height="1168" fill="none" stroke="var(--frame)" stroke-width="4"/>
    <rect x="30" y="30" width="868" height="1140" fill="none" stroke="var(--frame)" stroke-width="1.5"/>
    <path d="M16 90 Q60 60 90 16" fill="none" stroke="var(--frame)" stroke-width="2"/>
    <path d="M912 90 Q868 60 838 16" fill="none" stroke="var(--frame)" stroke-width="2"/>
  </svg>

  <h1 class="brand">The Copper Lantern</h1>

  <p class="headline headline--dishes">Steaks &bull; Fish &bull; Chicken</p>
  <p class="headline headline--method">Cooked on an Open Flame!</p>
  <p class="headline headline--hours">Open All Day!</p>

  <div class="premises-photo" role="img" aria-label="Photo of the restaurant frontage with its entrance and sign"></div>

  <p class="offer offer--breakfast">Breakfast</p>
  <p class="offer offer--lunch">Lunch</p>
  <p class="offer offer--ales">Cask<br>Ales</p>
  <p class="offer offer--cakes">Cakes &amp;<br>Coffees</p>
  <p class="offer offer--buffet">Buffet</p>
  <p class="offer offer--wines">Fine<br>Wines</p>

  <p class="contact">Address/phone<br>Web site goes here</p>
</main>
</body>
</html>
```